Images and design ideas provided: Postcard size flier

2 sided postcard size flier to hand people on the street.

A FUN tax business needs a postcard size flier to hand people on the street. Not a typical serious, quiet, office so make the image fun!

Exact wording, logo and key images provided. You are free to add other images as you see fit (such as money).

Side 1: Use image of lady looking up (she should be looking at text provided).All spanish and english text provided. Logo in bottom right corner. Address at bottom of card.

Side 2: Image of lady holding money and pointing. Remove money and have her holding a sign/or some other creative way to have her looking at text. All spanish and english text provided. Logo in bottom right corner. Address at bottom of card.

Size: 4" x 6" horizontal or vertical is ok
Each side can be different and image/design does not have to be related.

Target Market(s)

Age 18-35

Industry/Entity Type

Accounting

Font styles to use
Sans Serif

Colors

Designer to choose colors to be used in the design.

Requirements
Must have
• Use text document provided. All text goes on both sides.
• Should be easy to read from a few feet away.
Nice to have
• Bright colors to attract attention of people walking by to grab flier/card. Images of money ok.
Should not have
• No images of calculators or typical accounting tax forms.

```html
<!DOCTYPE html>
<html lang="en">
<head>
<meta charset="utf-8">
<title>Refund Harbor – $100 Cash Now Fliers</title>
<link rel="stylesheet" href="https://fonts.googleapis.com/css2?family=Oswald:wght@500;600&family=Roboto:wght@400;500&display=swap">
<style>
  :root {
    --stage: #3b3b3d;
    --paper: #ffffff;
    --blue: #5a86c9;
    --blue-ink: #3d6db8;
    --red: #e8173f;
    --salmon: #f0746d;
    --footer: #060606;
    --white: #ffffff;
    --photo-a: #f4f1ea;
    --photo-b: #8f9a6a;
    --photo-c: #c9a85a;
  }
  * { box-sizing: border-box; margin: 0; padding: 0; }
  html, body {
    width: 1200px; height: 776px; overflow: hidden;
    background: var(--stage);
  }
  .canvas {
    position: relative; width: 1200px; height: 776px;
    display: flex; justify-content: center; align-items: center; gap: 40px;
  }
  .flier {
    position: relative; width: 430px; height: 640px;
    background: var(--paper); overflow: hidden;
    font-family: "Oswald", sans-serif;
  }
  .headline {
    font-weight: 600; font-size: 46px; line-height: 1; text-transform: uppercase;
    text-align: center; letter-spacing: 0.5px;
  }
  .headline .amount { font-size: 58px; }
  .subline {
    font-weight: 600; font-size: 21px; text-transform: uppercase; text-align: center; margin-top: 6px;
  }
  /* Side 1 */
  .flier--blue .header-band {
    position: absolute; top: 0; left: 0; right: 0; height: 130px;
    background: var(--blue); color: var(--white);
    display: flex; flex-direction: column; justify-content: center; padding-top: 6px;
  }
  .flier--blue .photo {
    position: absolute; top: 130px; left: 40px; right: 0; bottom: 100px;
    background: radial-gradient(ellipse at 55% 60%, var(--photo-b) 0%, var(--photo-c) 30%, var(--photo-a) 68%, var(--paper) 100%);
  }
  .spanish-corner {
    position: absolute; left: 22px; bottom: 118px; color: var(--blue-ink);
    text-transform: uppercase;
  }
  .spanish-corner .lead { font-weight: 600; font-size: 24px; line-height: 1.15; }
  .spanish-corner .small { font-weight: 500; font-size: 13px; line-height: 1.3; margin-top: 4px; }
  /* Side 2 */
  .flier--red .title-block {
    position: absolute; top: 34px; left: 0; right: 0; color: var(--red);
  }
  .flier--red .photo {
    position: absolute; top: 140px; left: 20px; right: 20px; bottom: 170px;
    background: radial-gradient(ellipse at 45% 60%, var(--photo-b) 0%, var(--photo-c) 32%, var(--photo-a) 70%, var(--paper) 100%);
  }
  .spanish-band {
    position: absolute; left: 0; right: 0; bottom: 85px; height: 85px;
    background: var(--salmon); color: var(--white); text-transform: uppercase; text-align: center;
    display: flex; flex-direction: column; justify-content: center;
  }
  .spanish-band .lead { font-weight: 600; font-size: 27px; line-height: 1.1; }
  .spanish-band .small { font-weight: 500; font-size: 15px; margin-top: 4px; }
  /* Footer */
  .footer {
    position: absolute; left: 0; right: 0; bottom: 0;
    background: var(--footer); color: var(--white);
    display: flex; justify-content: space-between; align-items: center; padding: 0 22px;
  }
  .flier--blue .footer { height: 100px; }
  .flier--red .footer { height: 85px; }
  .contact { font-family: "Roboto", sans-serif; }
  .contact .address { font-size: 13px; font-weight: 400; }
  .contact .phone { font-size: 19px; font-weight: 500; margin-top: 6px; }
  .brand {
    font-family: "Oswald", sans-serif; font-weight: 600; font-size: 22px;
    color: var(--red); text-transform: uppercase; line-height: 1; letter-spacing: 1px;
    display: flex; align-items: center; gap: 10px;
  }
  .brand .mark { width: 14px; height: 14px; background: var(--red); }
</style>
</head>
<body>
<main class="canvas">
  <section class="flier flier--blue" aria-label="Flier side one">
    <header class="header-band">
      <h1 class="headline">Get <span class="amount">$100</span> Cash Now!</h1>
      <p class="subline">With paid tax preparation</p>
    </header>
    <div class="photo" role="img" aria-label="Woman in a royal costume and crown looking up at falling dollar bills, with a gift box full of money"></div>
    <div class="spanish-corner">
      <p class="lead">Reciba $100 en<br>efectivo ahora!</p>
      <p class="small">Con la preparacion<br>pagada de sus impuestos</p>
    </div>
    <footer class="footer">
      <div class="contact">
        <p class="address">418 Maple Ave. Riverton NY 10000</p>
        <p class="phone">(555) 014-0199</p>
      </div>
      <div class="brand"><span class="mark"></span><span>Refund<br>Harbor</span></div>
    </footer>
  </section>

  <section class="flier flier--red" aria-label="Flier side two">
    <div class="title-block">
      <h1 class="headline">Get <span class="amount">$100</span> Cash Now!</h1>
      <p class="subline">With paid tax preparation</p>
    </div>
    <div class="photo" role="img" aria-label="Woman in a royal costume and crown pointing at a fan of dollar bills in her hand"></div>
    <div class="spanish-band">
      <p class="lead">Reciba $100 en efectivo ahora!</p>
      <p class="small">Con la preparacion pagada de sus impuestos</p>
    </div>
    <footer class="footer">
      <div class="contact">
        <p class="address">418 Maple Ave. Riverton NY 10000</p>
        <p class="phone">(555) 014-0199</p>
      </div>
      <div class="brand"><span class="mark"></span><span>Refund<br>Harbor</span></div>
    </footer>
  </section>
</main>
</body>
</html>
```